Pack and Ship Business Model that caters to local community, county and state level in NorthCarolina

I currently have an outdated business card for my store that I am about to take over, this July 1st and wanted a fresh look on what their current one is like since the store is about 20 years old. Also the backside would need to have all the items that is listed and creatively well put together, the other design concept was not what i was looking for and frankly disappointed. All i ask is to please take your time with the project.

Target Market(s)

Mailing, Packing, Shipping, Consumers, Renters, Professionals, Trade Shows

Industry/Entity Type

Mailbox

Contact Information for Business Card

Double sided

Font styles to use
Serif

Colors
3277b5
33a6d7
85acd3
f04a50
fbf289

Requirements
Must have
• Below is a pick from Nice to Have, as my business does have alot of services that is being offered it is a premiere, mailing, shipping, packing, boxing, photo finishing, gift shop and more! Additionally it should have the logo that I have attached, but blue is preferred, I would need the logos for TRAVIQ, KLO, RVN, GMTB incorporated on the design as well as those are vendors that are part of my store services that i use for shipping/mailing.
Nice to have
• Boxes, Postage stamp, shipping label, customer service, friendly atmosphere, Mailboxes that is like in the KLO stores,
Should not have
• shipping trucks, geometric shapes

```html
<!DOCTYPE html>
<html lang="en">
<head>
<meta charset="utf-8">
<title>Swift Parcel &amp; Post – Business Card</title>
<link rel="stylesheet" href="https://fonts.googleapis.com/css2?family=Roboto:wght@400;500;700&family=Tinos:wght@400;700&display=swap">
<style>
  :root {
    --brand-blue: #2b3288;
    --card-white: #ffffff;
    --backdrop: #e4e4e2;
  }
  * { margin: 0; padding: 0; box-sizing: border-box; }
  html, body { width: 1200px; height: 801px; overflow: hidden; }
  body { background: var(--backdrop); position: relative; font-family: "Roboto", Arial, sans-serif; color: var(--brand-blue); }

  .card { position: absolute; top: 240px; width: 560px; height: 320px; background: var(--card-white); overflow: hidden; box-shadow: 0 6px 18px rgba(0,0,0,.18); }
  .card-front { left: 27px; }
  .card-back { left: 613px; background: var(--brand-blue); }

  .card-art { position: absolute; inset: 0; width: 100%; height: 100%; }

  /* Front */
  .brand-mark { position: absolute; display: flex; align-items: center; gap: 10px; font-family: "Tinos", "Times New Roman", serif; font-weight: 400; color: var(--brand-blue); line-height: 1; }
  .brand-mark .mark-dot { width: 14px; height: 14px; border-radius: 50%; background: var(--brand-blue); }
  .card-front .brand-mark { left: 352px; top: 34px; font-size: 56px; letter-spacing: 2px; }

  .vendor-list { position: absolute; left: 350px; top: 104px; display: grid; grid-template-columns: 78px 70px; gap: 6px 10px; }
  .vendor-name { font-family: "Roboto", Arial, sans-serif; font-weight: 700; font-size: 15px; color: var(--brand-blue); letter-spacing: .5px; }

  .contact-block { position: absolute; left: 36px; top: 56px; }
  .person-name { font-weight: 700; font-size: 24px; letter-spacing: .5px; text-transform: uppercase; }
  .person-title { font-size: 14px; margin-top: 2px; }
  .address { margin-top: 20px; font-size: 13.5px; line-height: 1.4; }
  .contact-list { list-style: none; font-size: 13.5px; line-height: 1.4; }
  .contact-list li { display: flex; align-items: center; gap: 7px; }
  .contact-icon { width: 13px; height: 13px; flex: none; }
  .social-square { width: 12px; height: 12px; background: var(--brand-blue); border-radius: 2px; flex: none; }

  /* Back */
  .services { position: absolute; left: 112px; top: 88px; font-family: "Tinos", "Times New Roman", serif; }
  .services-title { font-size: 24px; font-weight: 700; margin-bottom: 6px; }
  .services-list { list-style: none; font-size: 13px; line-height: 1.3; }
  .services-list li::before { content: "•"; margin-right: 6px; }
  .card-back .brand-mark { left: 320px; top: 80px; font-size: 60px; letter-spacing: 2px; }
</style>
</head>
<body>

<section class="card card-front" aria-label="Business card front">
  <svg class="card-art" viewBox="0 0 560 320" aria-hidden="true">
    <path d="M78,320 C150,205 430,240 560,150 L560,320 Z" fill="var(--brand-blue)"/>
  </svg>

  <div class="brand-mark"><span class="mark-dot"></span>SPP</div>

  <div class="vendor-list">
    <span class="vendor-name">TRAVIQ</span>
    <span class="vendor-name">RVN</span>
    <span class="vendor-name">KLO</span>
    <span class="vendor-name">GMTB</span>
  </div>

  <div class="contact-block">
    <h1 class="person-name">Marcus Ellery</h1>
    <p class="person-title">Managing Director</p>
    <p class="address">Cedar Row Plaza<br>4410-210 Maple Ferry Rd.<br>Durham, NC 27705</p>
    <ul class="contact-list">
      <li>
        <svg class="contact-icon" viewBox="0 0 16 16" aria-hidden="true"><path d="M4 1 L6.5 1 L7.5 5 L5.6 6.3 C6.5 8.3 7.7 9.5 9.7 10.4 L11 8.5 L15 9.5 L15 12 C15 13.6 13.6 15 12 15 C6 15 1 10 1 4 C1 2.4 2.4 1 4 1 Z" fill="var(--brand-blue)"/></svg>
        (919) 555-0142
      </li>
      <li>
        <svg class="contact-icon" viewBox="0 0 16 16" aria-hidden="true"><rect x="1" y="3" width="14" height="10" fill="var(--brand-blue)"/><path d="M1.5 3.5 L8 9 L14.5 3.5" fill="none" stroke="#fff" stroke-width="1.4"/></svg>
        hello@swiftparcelpost.com
      </li>
      <li>
        <span class="social-square"></span>
        Swift Parcel &amp; Post-Cedar Row
      </li>
    </ul>
  </div>
</section>

<section class="card card-back" aria-label="Business card back">
  <svg class="card-art" viewBox="0 0 560 320" aria-hidden="true">
    <path d="M0,0 L430,0 C520,70 545,220 495,320 L125,320 C75,295 52,230 52,150 C52,80 28,30 0,0 Z" fill="var(--card-white)"/>
  </svg>

  <div class="services">
    <h2 class="services-title">Services:</h2>
    <ul class="services-list">
      <li>Mailbox Rental And Virtual</li>
      <li>Shipping, Packaging</li>
      <li>Mail Same-day Pickup</li>
      <li>Print-copy-scan-fax</li>
      <li>Photo Print Shop</li>
      <li>Passport Photos</li>
      <li>Key Duplication</li>
      <li>Finishing Binding Services</li>
      <li>Notary Public Services</li>
      <li>Document Shredding</li>
    </ul>
  </div>

  <div class="brand-mark"><span class="mark-dot"></span>SPP</div>
</section>

</body>
</html>
```